Landing page for buying gold and stamps

Create a landing page for our purchase. We buy postage stamps, franked goods, gold coins, scrap gold, silver money, etc. We don't want to sell anything to people, we just shop. So the visitors should send their old gold, their stamps, etc. by post. We then estimate the value and transfer the money by bank or you can collect it in cash.

The visitor should see what he can sell. If he fills in his contact details, he will receive our purchase form and the mailing label by post so that he can send in his sales goods free of charge. Or he can call us or write an e-mail and come to us directly.

We buy:
When the form is filled out, an email will be sent to our address with the following data:
Surname
First name
Street, Nr.
Post loan number
place
What do you want to sell

In the appendix I have added designs of flyers. You can see what we buy on it. What is missing on the flyer, however, are stamps, franking goods and rarities. In addition, the design should be similar. The logo can also be used.

In addition, the following text should be on the page:
Do you need help selling an inherited collection? Feel free to contact us. We are happy to help. We have been in the stamp and coin trade for nearly 100 years.

I have also attached a picture of the stamp as an attachment. This should also be put on the side with old gold and gold coins.

And here you will find our current purchase pages:
https://www.briefhaus-tanner.ch/ankauf-gold-und-silber
https://www.briefhaus-tanner.ch/ankauf-frankatur

Competitors' pages:
https://www.edelwertplatz.ch/goldankauf/
https://www.talerbruhin.ch/ankauf-1/altgold-ankauf1.html?gclid=Xq7RtLwPzN2vKdFaYbHsUmEcGjTnQoVrZiBxWkLpDyAsCfNhMuJbOeTgIlKwSvHaRdYqPzXnBmCtGuFoLiEkJrQsWvTy

Target Market(s)

Private persons

Font styles to use
Serif
Sans Serif

Requirements
Must have
• It must be clear that anyone who wants to sell their gold, stamps or coins can do so easily from home by post. You no longer have to go to a store.
Steps to Sell:
1. You fill out your contact details
2. We will send you a form and a label for shipping (no postage for you!)
3. You will receive a non-binding purchase offer
4. You will receive the money transferred or you can collect it in cash (or we will send you the valuables you have sent back)

You have no costs! Simply sell your gold or stamps from home.

```html
<!DOCTYPE html>
<html lang="en">
<head>
<meta charset="utf-8">
<title>Briefhaus Tanner – We Buy Gold, Coins &amp; Stamps</title>
<link rel="stylesheet" href="https://fonts.googleapis.com/css2?family=Roboto:wght@400;500;700;900&family=Cinzel:wght@400;700&display=swap">
<style>
:root{
  --navy:#27218c;
  --night:#0b0a1d;
  --gold:#c28b33;
  --red:#c8121c;
  --ink:#222;
  --white:#fff;
}
*{box-sizing:border-box;margin:0;padding:0}
html,body{width:1200px;height:2474px;overflow:hidden}
body{position:relative;font-family:'Roboto',sans-serif;color:var(--ink);background:var(--white)}
.abs{position:absolute}
/* header */
.brand{left:110px;top:38px;font-family:'Roboto',sans-serif;font-weight:900;font-size:24px;color:var(--navy);letter-spacing:1px;display:flex;align-items:center;gap:10px}
.brand .mark{width:18px;height:18px;background:var(--red)}
.top-links{left:545px;top:51px;display:flex;gap:34px;font-size:14px;color:#333}
.search{left:1050px;top:48px}
.main-nav{left:0;top:113px;width:1200px;height:66px;background:var(--navy);display:flex;justify-content:center;align-items:center;gap:52px;color:var(--white);font-size:14px}
/* hero */
.hero{left:0;top:179px;width:1200px;height:599px;background:var(--night)}
.hero-photo{left:643px;top:288px;width:557px;height:466px;border-radius:45% 10% 40% 30%;background:radial-gradient(ellipse at 45% 50%,#e3b94f 0%,#b58326 45%,#7a5418 70%,rgba(11,10,29,0) 100%)}
.hero-copy{left:363px;transform:translateX(-50%);text-align:center;color:var(--white);width:560px}
.hero-q{top:311px;font-size:22px;font-weight:700}
.hero-title{top:358px;font-family:'Cinzel',serif;font-weight:700;font-size:62px;color:var(--red);line-height:1}
.hero-sub{top:437px;font-family:'Cinzel',serif;font-size:26px}
.hero-phone{top:470px;font-size:52px;font-weight:700;letter-spacing:1px}
.btn{background:var(--gold);color:var(--white);border-radius:34px;font-weight:700;font-size:32px;display:flex;align-items:center;justify-content:center}
.hero-btn{left:212px;top:555px;width:303px;height:64px}
.dot{top:695px;width:13px;height:13px;border-radius:50%;background:var(--white)}
.dot.on{background:var(--gold)}
/* intro */
.intro-title{left:0;top:822px;width:1200px;text-align:center;font-weight:700;font-size:62px;line-height:76px;color:var(--gold)}
.intro-link{left:0;top:973px;width:1200px;text-align:center;font-size:27px;font-weight:500;color:var(--red);text-decoration:underline}
.intro-text{left:0;top:1016px;width:1200px;text-align:center;font-size:24px;color:#333}
/* steps */
.steps{left:0;top:1075px;width:1200px;height:200px;background:var(--gold)}
.step{top:1107px;width:220px;margin-left:-110px;text-align:center;color:var(--white);font-size:17px;line-height:21px}
.step svg{display:block;margin:0 auto 12px}
.divider{top:1098px;width:1px;height:162px;background:rgba(255,255,255,.35)}
/* form */
.panel{left:300px;top:1352px;width:600px;height:635px;background:var(--night)}
.tab{left:300px;top:1352px}
.tab-label{left:472px;top:1380px;width:256px;text-align:center;font-size:32px;font-weight:700;color:var(--ink)}
.panel-text{left:360px;top:1468px;width:480px;text-align:center;color:var(--white);font-size:16.5px;line-height:21px}
.field{background:var(--white);font-size:16px;color:#333;padding:12px 20px}
.submit{left:448px;top:1885px;width:303px;height:64px;border-radius:34px}
.photo-pouch{left:168px;top:1335px;width:208px;height:130px;border-radius:50%;background:radial-gradient(ellipse at 40% 45%,#2c2c2c 0%,#3a3a3a 35%,#d4b14a 60%,rgba(255,255,255,0) 75%)}
.photo-stamp{left:208px;top:1872px;width:196px;height:126px;transform:rotate(17deg);background:linear-gradient(135deg,#ece6d6,#cfc1a0 60%,#b9a77f)}
.photo-jewel{left:720px;top:1815px;width:290px;height:245px;border-radius:40% 20% 45% 45%;background:radial-gradient(ellipse at 50% 60%,#d8ad42 0%,#b27f22 50%,rgba(255,255,255,0) 78%),linear-gradient(160deg,#6f7fa6 0%,#b8475a 30%,rgba(255,255,255,0) 45%)}
/* footer */
.footer{left:0;top:2083px;width:1200px;height:391px;background:radial-gradient(ellipse at 30% 60%,#2b2418 0%,#171310 50%,#0c0a09 100%)}
.contact-bar{left:0;top:2145px;width:1200px;display:flex;justify-content:center;gap:36px}
.contact-row{display:flex;align-items:center;gap:16px;color:var(--white);font-size:18px;white-space:nowrap}
.footer-rule{left:0;top:2208px;width:1200px;height:1px;background:rgba(255,255,255,.12)}
.col-head{top:2254px;color:var(--white);font-size:21px;font-weight:400}
.col-links{top:2307px;list-style:none;color:var(--white);font-size:16px;line-height:41px}
.col-links li::before{content:"›";margin-right:18px;margin-left:8px}
.foot-brand{left:869px;top:2270px;color:var(--white);font-weight:900;font-size:24px;letter-spacing:1px;display:flex;align-items:center;gap:10px}
.foot-brand .mark{width:18px;height:18px;background:var(--white)}
.social{top:2369px;width:24px;height:24px;border-radius:50%;border:2px solid var(--white)}
.copyright{left:874px;top:2408px;color:var(--white);font-size:14px}
.code{left:1127px;top:2411px;color:var(--white);font-size:10px}
</style>
</head>
<body>

<header>
  <div class="abs brand"><span class="mark"></span>BRIEFHAUS TANNER</div>
  <nav class="abs top-links"><span>My user account</span><span>My wish list</span><span>My Cart</span><span>Checkout</span><span>Register</span></nav>
  <svg class="abs search" width="24" height="24" viewBox="0 0 24 24"><circle cx="10" cy="10" r="7" fill="none" stroke="#111" stroke-width="3"/><line x1="15" y1="15" x2="22" y2="22" stroke="#111" stroke-width="3.5" stroke-linecap="round"/></svg>
  <nav class="abs main-nav"><span>Postage Stamps</span><span>Tanner - albums accessories</span><span>Coins &nbsp;&amp; Banknotes</span><span>Missing List Service</span><span>Franking Service</span></nav>
</header>

<section>
  <div class="abs hero"></div>
  <div class="abs hero-photo" role="img" aria-label="Hand holding gold coins, jewellery and an old stamp"></div>
  <p class="abs hero-copy hero-q">Do you need help selling an inherited collection?</p>
  <h1 class="abs hero-copy hero-title">Gold &amp; Silver</h1>
  <p class="abs hero-copy hero-sub">Feel Free To Contact Us</p>
  <p class="abs hero-copy hero-phone">0041 61 480 27 15</p>
  <div class="abs btn hero-btn">Get in Touch</div>
  <span class="abs dot" style="left:567px"></span>
  <span class="abs dot on" style="left:594px"></span>
  <span class="abs dot" style="left:620px"></span>
</section>

<section>
  <h2 class="abs intro-title">Do you need help selling an<br>inherited collection?</h2>
  <p class="abs intro-link">Feel free to contact us</p>
  <p class="abs intro-text">We are happy to help. We have been in the stamp and coin trade for nearly 100 years.</p>
</section>

<section>
  <div class="abs steps"></div>
  <span class="abs divider" style="left:351px"></span>
  <span class="abs divider" style="left:591px"></span>
  <span class="abs divider" style="left:824px"></span>
  <div class="abs step" style="left:223px">
    <svg width="40" height="42" viewBox="0 0 40 42"><circle cx="20" cy="11" r="10" fill="#fff"/><path d="M2 42v-6c0-8 7-13 18-13s18 5 18 13v6z" fill="#fff"/></svg>
    You fill out your<br>contact details</div>
  <div class="abs step" style="left:472px">
    <svg width="46" height="42" viewBox="0 0 46 42"><path d="M1 3h8l6 26h24l5-19H12" fill="none" stroke="#fff" stroke-width="4" stroke-linejoin="round"/><path d="M14 10h29l-4 17H18z" fill="#fff"/><path d="M28 12v12M22 18h12" stroke="#c28b33" stroke-width="3"/><circle cx="19" cy="37" r="4" fill="#fff"/><circle cx="36" cy="37" r="4" fill="#fff"/></svg>
    We will send you<br>a form and a label<br>for shipping</div>
  <div class="abs step" style="left:707px">
    <svg width="34" height="42" viewBox="0 0 34 42"><path d="M0 0h22l12 12v30H0z" fill="#fff"/><path d="M22 0v12h12" fill="#e8cfa0"/><path d="M6 16h12M6 22h22v8H6zM6 34h22" stroke="#c28b33" stroke-width="2.5" fill="none"/></svg>
    You will receive a<br>non-binding<br>purchase offer</div>
  <div class="abs step" style="left:954px">
    <svg width="52" height="42" viewBox="0 0 52 42"><rect x="2" y="7" width="48" height="28" rx="3" fill="none" stroke="#fff" stroke-width="4"/><path d="M2 14a7 7 0 0 0 7-7M43 7a7 7 0 0 0 7 7M2 28a7 7 0 0 1 7 7M50 28a7 7 0 0 0-7 7" fill="#fff" stroke="#fff" stroke-width="3"/><circle cx="26" cy="21" r="9" fill="#fff"/><path d="M24 17l3-1v10" stroke="#c28b33" stroke-width="2.5" fill="none"/></svg>
    You will receive<br>the money transferred<br>or you can collect<br>it in cash</div>
</section>

<section>
  <div class="abs panel"></div>
  <svg class="abs tab" width="600" height="90" viewBox="0 0 600 90"><polygon points="172,0 428,0 396,88 204,88" fill="#fff"/></svg>
  <h2 class="abs tab-label">WE BUY</h2>
  <div class="abs photo-pouch" role="img" aria-label="Velvet pouch spilling gold coins"></div>
  <p class="abs panel-text">When the form is filled out, an email will be sent to our address with the following dataWhen the form is filled out, an email will be sent to our address with the following data</p>
  <div class="abs field" style="left:343px;top:1569px;width:247px;height:44px">Surname</div>
  <div class="abs field" style="left:609px;top:1569px;width:247px;height:44px">First name</div>
  <div class="abs field" style="left:343px;top:1630px;width:247px;height:44px">Street, Nr</div>
  <div class="abs field" style="left:609px;top:1630px;width:247px;height:44px">Post loan number</div>
  <div class="abs field" style="left:343px;top:1692px;width:513px;height:48px;padding-left:24px">Place</div>
  <div class="abs field" style="left:343px;top:1759px;width:513px;height:100px;padding-left:24px;padding-top:16px">What do you want to sell</div>
  <div class="abs photo-stamp" role="img" aria-label="Vintage postage stamp"></div>
  <div class="abs photo-jewel" role="img" aria-label="Gold jewellery, coins and a classic stamp"></div>
  <div class="abs btn submit">Submit</div>
</section>

<footer>
  <div class="abs footer" role="img" aria-label="Dark background of gold jewellery"></div>
  <div class="abs contact-bar">
    <div class="contact-row">
      <svg width="24" height="24" viewBox="0 0 24 24" fill="none" stroke="#fff" stroke-width="2"><circle cx="12" cy="12" r="10"/><ellipse cx="12" cy="12" rx="4.5" ry="10"/><path d="M2 12h20M4 6.5h16M4 17.5h16"/></svg>www.briefhaus-tanner.ch</div>
    <div class="contact-row">
      <svg width="26" height="20" viewBox="0 0 26 20"><rect width="26" height="20" rx="2" fill="#fff"/><path d="M1 2l12 9 12-9" fill="none" stroke="#1a1612" stroke-width="2"/></svg>info@briefhaus-tanner.ch</div>
    <div class="contact-row">
      <svg width="20" height="26" viewBox="0 0 20 26"><path d="M10 0a9 9 0 0 1 9 9c0 7-9 17-9 17S1 16 1 9a9 9 0 0 1 9-9z" fill="#fff"/><circle cx="10" cy="9" r="3.5" fill="#1a1612"/></svg>Werkhofweg 9, 4318 Lindmatt</div>
  </div>
  <div class="abs footer-rule"></div>

  <h3 class="abs col-head" style="left:140px">Customer service</h3>
  <ul class="abs col-links" style="left:140px"><li>Guarantee of trust</li><li>Shipping</li></ul>
  <h3 class="abs col-head" style="left:364px">Contact</h3>
  <ul class="abs col-links" style="left:364px"><li>Contact</li><li>Imprint</li></ul>
  <h3 class="abs col-head" style="left:544px">Information</h3>
  <ul class="abs col-links" style="left:544px"><li>Conditions</li><li>Revocation</li><li>Data protection</li></ul>

  <div class="abs foot-brand"><span class="mark"></span>BRIEFHAUS TANNER</div>
  <span class="abs social" style="left:962px" aria-label="Social profile"></span>
  <span class="abs social" style="left:1014px" aria-label="Social profile"></span>
  <span class="abs social" style="left:1071px" aria-label="Social profile"></span>
  <p class="abs copyright">©&nbsp; 2020 &nbsp;| &nbsp;www.briefhaus-tanner.ch</p>
  <p class="abs code">M1</p>
</footer>

</body>
</html>
```